Re-design of Business Card

We require a design for our business card.

Quorin is a supplier of industrial packaging specializing in plastic products. We are undergoing a rebranding to appear more corporate. We have changed our company name to quorin and have a new logo.

I have uploaded our old card design with the previous company name.
Don't copy the current design. We are looking for a new design.

Industry/Entity Type

Manufacturing

Contact Information for Business Card

please don't copy the current design. we are looking for a new design.

Font styles to use
Sans Serif

Colors

Designer to choose colors to be used in the design.

Requirements
Must have
• clean and easy to read.

```html
<!DOCTYPE html>
<html lang="en">
<head>
<meta charset="utf-8">
<title>Quorin Business Card</title>
<link href="https://fonts.googleapis.com/css2?family=Lato:wght@400;700;900&display=swap" rel="stylesheet">
<style>
  :root {
    --stage: #3a3532;
    --card: #111111;
    --card-edge: #1c1c1c;
    --accent: #f28a1e;
    --text: #d8d8d8;
    --muted: #bdbdbd;
    --silver: #d6d6d6;
    --divider: #262626;
  }
  * { box-sizing: border-box; margin: 0; padding: 0; }
  html, body {
    width: 1200px; height: 844px; overflow: hidden;
    background: var(--stage);
    font-family: "Lato", Arial, sans-serif;
  }
  .canvas {
    width: 1200px; height: 844px;
    display: flex; align-items: center; justify-content: center; gap: 60px;
  }
  .card {
    position: relative;
    width: 525px; height: 300px;
    background: var(--card);
    border: 1px solid var(--card-edge);
    border-radius: 4px;
    box-shadow: 0 10px 30px rgba(0,0,0,.45);
  }
  /* contact side */
  .card-back .brand {
    position: absolute; left: 50px; top: 50%;
    transform: translateY(-50%);
    font-weight: 900; font-size: 52px; letter-spacing: 1px;
    color: var(--accent);
  }
  .card-back .divider {
    position: absolute; left: 292px; top: 40px; bottom: 40px;
    width: 1px; background: var(--divider);
  }
  .contact {
    position: absolute; left: 310px; top: 48px; right: 20px;
  }
  .contact .name {
    font-weight: 700; font-size: 17px; color: var(--accent);
    letter-spacing: .3px;
  }
  .contact .role {
    font-size: 12.5px; color: var(--muted); margin-bottom: 10px;
  }
  .contact-list { list-style: none; }
  .contact-list li {
    display: flex; align-items: center; gap: 8px;
    font-size: 13px; color: var(--text); line-height: 19px;
  }
  .contact-list svg { width: 10px; height: 10px; fill: var(--accent); flex: none; }
  .contact .address {
    margin-top: 10px; font-size: 13px; line-height: 18px; color: var(--text);
  }
  /* logo side */
  .card-front { display: flex; align-items: center; justify-content: center; }
  .card-front .brand {
    font-weight: 900; font-size: 58px; letter-spacing: 1px;
    color: var(--silver);
  }
</style>
</head>
<body>
<main class="canvas">
  <section class="card card-back" aria-label="Card contact side">
    <div class="brand">QUORIN</div>
    <div class="divider"></div>
    <div class="contact">
      <p class="name">DORIAN WELLES</p>
      <p class="role">Machinery Sales Manager</p>
      <ul class="contact-list">
        <li><svg viewBox="0 0 10 10"><path d="M2 0h2l1 2.5-1.3 1a6 6 0 0 0 2.8 2.8l1-1.3L10 6v2a2 2 0 0 1-2 2A8 8 0 0 1 0 2a2 2 0 0 1 2-2z"/></svg>1300 555 014</li>
        <li><svg viewBox="0 0 10 10"><path d="M2.5 0h5a1 1 0 0 1 1 1v8a1 1 0 0 1-1 1h-5a1 1 0 0 1-1-1V1a1 1 0 0 1 1-1zm.5 1.5v6h4v-6z"/></svg>XXXX XXX XXX</li>
        <li><svg viewBox="0 0 10 10"><path d="M2 0h6v3H2zM0 3.5h10v4.5H8V10H2V8H0zm3 3V9h4V6.5z"/></svg>+61 75550 1287</li>
        <li><svg viewBox="0 0 10 10"><path d="M0 2h10v6H0zm1 1v.3l4 2.5 4-2.5V3z"/></svg>dorian@quorin.com.au</li>
        <li><svg viewBox="0 0 10 10"><circle cx="5" cy="5" r="5"/></svg>www.brenlowpack.com.au</li>
      </ul>
      <p class="address">48 Tarrant Rd Redvale<br>Hills, WA 6931 Australia</p>
    </div>
  </section>
  <section class="card card-front" aria-label="Card logo side">
    <div class="brand">QUORIN</div>
  </section>
</main>
</body>
</html>
```